Business card design for Velvet Harbor

We need business cards designed for our new marketing consulting company, Velvet Harbor. Our services include marketing strategy, go-to-market and launch planning, growth strategy, and execution. We serve medical technology and health technology companies, from startups to well-established growth companies.

The business cards should feel professional, credible, reliable and trustworthy, and should instill confidence. Also bold, creative, and modern.

The design must use the Velvet Harbor logo.

The primary brand color is this orange: #FF5501
A secondary color that you can use is this gray: #282B2D
I would prefer only to use the orange and gray. But if you feel you really need an additional accent color (please use it very sparingly, as little as possible), you can use this blue for small accent purposes: #009FED

Attached are the logo files. The main logo is the one with a little bit of orange on the left and the rest is gray.

The business card should include the following:

Velvet Harbor logo
First name and last name
Title
Email address
Phone number and type (in whatever order looks best for the design
Website (the website does not need to be in the same block as the personal info)

For example:

Nessa Pryle
Founder & Principal
nessa@velvetharbor.com
+1.628.309.4156 mobile (can use "." or spaces in between blocks of numbers)
velvetharbor.com (somewhere on the card, it does not need to be with the personal info; and note that there is no "www." at the beginning)

Note that there will be no address listed on the business card.

Target Market(s)

Executives (CEO, head of marketing, head of sales) at medical technology and health technology companies, mostly in their 40s and older, well-educated, often with advanced degrees. They are strategic thinkers, responsible for budgets, and familiar with P&L. Their comfort with and trust in using outside consultants varies.

Industry/Entity Type

Medical technology and health technology companies.

Contact Information for Business Card

See project description

Font styles to use
Sans Serif

Requirements
Must have
• Logo and see Business card details section above.

```html
<!DOCTYPE html>
<html lang="en">
<head>
<meta charset="utf-8">
<title>Velvet Harbor — Business Card</title>
<link href="https://fonts.googleapis.com/css2?family=Arimo:wght@400;700&display=swap" rel="stylesheet">
<style>
  :root{
    --orange:#FF5501;
    --edge:#E04A00;
    --gray:#282B2D;
    --text-gray:#5E6163;
    --card-white:#F4F4F4;
    --card-dark:#2E2E2E;
    --backdrop:#E6E6E4;
  }
  *{margin:0;padding:0;box-sizing:border-box}
  html,body{width:1200px;height:801px;overflow:hidden;background:var(--backdrop);font-family:"Arimo",Arial,sans-serif}
  .stage{position:relative;width:1200px;height:801px}
  .card{position:absolute;width:525px;height:300px;border-bottom:4px solid var(--edge);border-right:3px solid var(--edge);box-shadow:0 8px 22px rgba(0,0,0,.16)}
  .card--front{left:50px;top:250px;background:var(--card-white)}
  .card--back{left:622px;top:250px;background:var(--card-dark)}

  .brand{position:absolute;display:flex;align-items:center;gap:14px}
  .brand__dot{width:14px;height:14px;border-radius:50%;background:var(--orange);flex:none}
  .brand__name{font-weight:700;letter-spacing:.22em;line-height:1.12;text-transform:uppercase}
  .card--front .brand{left:112px;top:70px}
  .card--front .brand__name{font-size:24px;color:var(--gray)}

  .person{position:absolute;left:112px;top:182px;text-align:right;width:150px}
  .person__name{font-size:20px;font-weight:700;color:var(--orange);line-height:1.15}
  .person__title{font-size:13px;color:var(--text-gray);margin-top:4px}
  .divider{position:absolute;left:278px;top:176px;width:1px;height:62px;background:#8A8C8E}
  .contact{position:absolute;left:294px;top:176px;list-style:none}
  .contact__item{display:flex;align-items:center;gap:8px;font-size:12.5px;color:var(--text-gray);height:21px}
  .contact__icon{width:12px;height:12px;flex:none}

  .card--back .brand{right:40px;bottom:44px}
  .card--back .brand__name{font-size:28px;color:#FFFFFF;text-align:left}
</style>
</head>
<body>
<main class="stage">
  <section class="card card--front" aria-label="Business card front">
    <div class="brand">
      <span class="brand__dot"></span>
      <span class="brand__name">Velvet<br>Harbor</span>
    </div>
    <div class="person">
      <p class="person__name">Nessa Pryle</p>
      <p class="person__title">Founder &amp; Principal</p>
    </div>
    <div class="divider"></div>
    <ul class="contact">
      <li class="contact__item">
        <svg class="contact__icon" viewBox="0 0 12 12"><path d="M2.5 1h2l1 2.6-1.3.9a6 6 0 0 0 3.3 3.3l.9-1.3 2.6 1v2A1.5 1.5 0 0 1 9.5 11 8.5 8.5 0 0 1 1 2.5 1.5 1.5 0 0 1 2.5 1z" fill="var(--orange)"/></svg>
        +1.628.309.4156
      </li>
      <li class="contact__item">
        <svg class="contact__icon" viewBox="0 0 12 12"><rect x=".8" y="2.3" width="10.4" height="7.4" rx=".8" fill="none" stroke="var(--orange)" stroke-width="1.2"/><path d="M1.2 2.8 6 6.6l4.8-3.8" fill="none" stroke="var(--orange)" stroke-width="1.2"/></svg>
        nessa@velvetharbor.com
      </li>
      <li class="contact__item">
        <svg class="contact__icon" viewBox="0 0 12 12"><circle cx="6" cy="6" r="5.2" fill="none" stroke="var(--orange)" stroke-width="1.1"/><ellipse cx="6" cy="6" rx="2.2" ry="5.2" fill="none" stroke="var(--orange)" stroke-width="1"/><path d="M.8 6h10.4M1.8 3.3h8.4M1.8 8.7h8.4" stroke="var(--orange)" stroke-width="1"/></svg>
        velvetharbor.com
      </li>
    </ul>
  </section>

  <section class="card card--back" aria-label="Business card back">
    <div class="brand">
      <span class="brand__name">Velvet<br>Harbor</span>
    </div>
  </section>
</main>
</body>
</html>
```